Yard Sign Design Needed

Yard sign needed for mowing & landscaping company. Would like to use the top logo with black background which is attached. Would like MOWING to be in large standout letters. The word "landscaping" can be smaller and more artistic or omitted. Will need room for phone number once design is approved. The phone number will need to stand out and look identical/similar to the word 'MOWING"

```html
<!DOCTYPE html>
<html lang="en">
<head>
<meta charset="utf-8">
<title>Brenlow Contractors – Mowing Yard Sign</title>
<link rel="stylesheet" href="https://fonts.googleapis.com/css2?family=Montserrat:wght@600;700;800;900&display=swap">
<style>
  :root {
    --sign-black: #060606;
    --lime: #b5cc2e;
    --white: #ffffff;
    --ink: #111111;
    --backdrop: #e9ebe6;
  }
  * { margin: 0; padding: 0; box-sizing: border-box; }
  html, body {
    width: 1200px;
    height: 601px;
    overflow: hidden;
  }
  body {
    background: var(--backdrop);
    font-family: "Montserrat", Arial, sans-serif;
    position: relative;
  }
  .yard-sign {
    position: absolute;
    left: 400px;
    top: 0;
    width: 400px;
    height: 601px;
    background: var(--sign-black);
    overflow: hidden;
  }
  .brand {
    position: absolute;
    top: 40px;
    left: 0;
    width: 100%;
    text-align: center;
  }
  .brand-square {
    display: block;
    width: 108px;
    height: 108px;
    margin: 0 auto 64px;
    background: var(--lime);
  }
  .brand-name {
    color: var(--white);
    font-weight: 700;
    font-size: 26px;
    line-height: 1.2;
    letter-spacing: 1px;
    text-transform: uppercase;
  }
  .service-arrow {
    position: absolute;
    left: 0;
    top: 360px;
    width: 384px;
    height: 96px;
  }
  .service-main {
    position: absolute;
    left: 28px;
    top: 378px;
    color: var(--white);
    font-weight: 900;
    font-size: 50px;
    letter-spacing: 0;
    line-height: 1;
    text-shadow: 2px 3px 3px rgba(0,0,0,0.75);
  }
  .service-sub {
    position: absolute;
    left: 30px;
    top: 438px;
    color: var(--white);
    font-weight: 800;
    font-size: 24px;
    line-height: 1;
  }
  .phone-band {
    position: absolute;
    left: 0;
    bottom: 0;
    width: 400px;
    height: 60px;
  }
  .phone-number {
    position: absolute;
    left: 26px;
    bottom: 10px;
    color: var(--ink);
    font-weight: 900;
    font-size: 37px;
    letter-spacing: 0.5px;
    line-height: 1;
    white-space: nowrap;
  }
</style>
</head>
<body>
  <main class="yard-sign">
    <header class="brand">
      <span class="brand-square" aria-hidden="true"></span>
      <p class="brand-name">Brenlow<br>Contractors<br>LLC</p>
    </header>

    <svg class="service-arrow" viewBox="0 0 384 96" aria-hidden="true">
      <polygon points="0,18 298,18 298,0 381,48 298,96 298,70 0,70" fill="var(--lime)"/>
    </svg>
    <h1 class="service-main">MOWING</h1>
    <p class="service-sub">Landscaping</p>

    <svg class="phone-band" viewBox="0 0 400 60" preserveAspectRatio="none" aria-hidden="true">
      <polygon points="0,0 380,0 400,60 0,60" fill="var(--white)"/>
    </svg>
    <p class="phone-number">00-555-764- 00</p>
  </main>
</body>
</html>
```